Corvane Lending Partners. Professional and Established Company

A full service finance company specializing in obtaining capital for small business. Business Lending advisor, helping small business owners access the capital they need to launch, grow, or sustain their business. Many of our programs offer flexible guidelines to overcome common obstacles such as credit score, credit history, and time in business, financials, and industry type. Our streamlined funding process makes getting a business loan, business line of credit, stated income commercial real estate loan, a smooth and stress free experience.SOME OF THE MOST COMMON NEEDS FOR BUSINESS CAPITAL:• Working Capital• Debt Consolidations (loans, merchant cash advances, etc.)• Payroll• Operating Expenses• Inventory• Equipment Financing• Commercial Real Estate (Purchase, Fix & Flip, Rehab, Renovations)• Business Acquisitions• Business ExpansionWe like the websites:www.brookfellcap.com they are in the same industry and provide the same servicesWe are wanting to be able to update when we do press releases and such using Word Press. Our look should be very professional and we will be adding Our Team Professional Bios and Headshots.

Industry/Entity Type

Finance

Number of Pages Required

5+ page

Font styles to use
Serif
Sans Serif

Requirements
Must have
• We want to copy brookfellcap.com
• We need:
• Home Page
• About Us
• Loan Programs
• Loan Criteria
• News
• Apply Now
• Contact
Nice to have
• See brookfellcap.com
Should not have
• Need professional design. Nothing bright or abstract

```html
<!DOCTYPE html>
<html lang="en">
<head>
<meta charset="utf-8">
<title>Corvane Lending Partners</title>
<link rel="stylesheet" href="https://fonts.googleapis.com/css2?family=Source+Sans+3:wght@300;400;600;700&display=swap">
<style>
:root{
  --blue:#1f6fe0;
  --blue-bright:#2a7cf0;
  --blue-soft:#4e9bf0;
  --blue-violet:#4a74e8;
  --ink:#222833;
  --muted:#555d68;
  --light:#f2f4f7;
  --pale:#e3f0fd;
  --dark:#1d1f22;
  --darker:#141517;
  --white:#ffffff;
}
*{box-sizing:border-box;margin:0;padding:0}
html,body{width:1200px;height:3167px;overflow:hidden}
body{position:relative;font-family:"Source Sans 3",sans-serif;color:var(--ink);background:var(--white)}
.abs{position:absolute}
a{color:inherit;text-decoration:none}

/* top bar */
.topbar{left:0;top:0;width:1200px;height:37px;background:var(--light);font-size:12px;color:#444}
.topbar .item{top:11px;display:flex;align-items:center;gap:6px}
.topbar b{font-weight:700;color:#222}
.social-dots{right:150px;top:11px;display:flex;gap:20px;align-items:center}
.social-dots span.dot{width:10px;height:10px;border-radius:50%;background:var(--blue)}

/* nav */
.nav{left:0;top:37px;width:1200px;height:64px;background:var(--white);box-shadow:0 1px 3px rgba(0,0,0,.08)}
.brand{left:150px;top:12px;display:flex;align-items:center;gap:8px}
.brand .mark{width:14px;height:14px;background:var(--blue)}
.brand .name{font-size:17px;font-weight:600;color:#2b5fb0;line-height:1.05;width:150px}
.menu{left:395px;top:23px;display:flex;gap:34px;font-size:12px;color:#333}
.menu .active{font-weight:600;color:#111}
.apply{left:971px;top:20px;width:78px;height:24px;background:var(--blue);color:#fff;font-size:11px;font-weight:600;display:flex;align-items:center;justify-content:center;border-radius:2px}

/* hero */
.hero{left:0;top:101px;width:1200px;height:514px;background:linear-gradient(100deg,#cfd4d8 0%,#8a8f96 30%,#b9bec4 55%,#6c737c 75%,#dfe3e6 100%)}
.hero-box{left:556px;top:266px;width:493px;height:252px;background:var(--blue-bright);color:#fff;padding:30px 20px}
.hero-box .lead{font-size:34px;font-weight:300;line-height:1.1}
.hero-box h1{font-size:38px;font-weight:700;line-height:1.15;margin-bottom:18px}
.hero-box p{font-size:13px;font-weight:600;line-height:1.2;margin-bottom:24px}
.btn-dark{display:inline-block;background:#2b2e33;color:#fff;font-size:12px;font-weight:600;padding:11px 15px}

/* features */
.feature{top:665px;width:270px;text-align:center}
.diamond{width:110px;height:110px;margin:20px auto 0;transform:rotate(45deg);background:var(--pale);box-shadow:0 8px 18px rgba(60,120,200,.15);display:flex;align-items:center;justify-content:center}
.diamond svg{transform:rotate(-45deg)}
.feature h3{margin-top:58px;font-size:16px;font-weight:400;color:#222}
.feature p{margin-top:16px;font-size:11px;line-height:22px;color:#555}

/* tiles */
.tile-photo-a{left:0;top:1033px;width:599px;height:602px;background:linear-gradient(135deg,#6a6f73 0%,#3e3a36 45%,#8a6e50 80%,#b8946a 100%)}
.deliver{left:150px;top:1283px;color:#fff}
.deliver h2{font-size:29px;font-weight:700;line-height:36px;letter-spacing:.3px}
.deliver p{font-size:20px;font-weight:600;margin-top:10px}
.btn-blue{display:inline-flex;align-items:center;gap:4px;background:var(--blue-bright);color:#fff;font-size:13px;font-weight:600;padding:11px 28px;margin-top:26px}
.tile-video{left:599px;top:1033px;width:318px;height:299px;background:linear-gradient(160deg,#56a6f3,#3f90ec);color:#fff;padding:72px 20px}
.tile-video h3{font-size:21px;font-weight:600}
.tile-video p{font-size:11px;line-height:22px;margin-top:8px;padding-left:6px}
.play{left:129px;top:182px}
.tile-grey{left:917px;top:1033px;width:283px;height:299px;background:var(--light);padding:75px 26px}
.tile-grey h3{font-size:21px;font-weight:600;line-height:23px;color:#111}
.tile-grey h3 span{color:var(--blue)}
.tile-grey p{font-size:11px;line-height:22px;color:#333;margin-top:12px}
.btn-outline{display:inline-flex;align-items:center;gap:4px;border:1px solid #555;font-size:11px;font-weight:600;color:#222;padding:9px 12px;margin-top:14px}
.tile-violet{left:599px;top:1332px;width:318px;height:303px;background:linear-gradient(160deg,#4d84ec,#4a6be4);color:#fff;padding:50px 24px}
.tile-violet h3{font-size:21px;font-weight:600;line-height:22px}
.tile-violet p{font-size:11px;line-height:22px;margin-top:10px}
.btn-white{display:inline-flex;align-items:center;gap:4px;background:#fff;color:var(--blue);font-size:11px;font-weight:700;padding:9px 12px;margin-top:34px}
.tile-photo-b{left:917px;top:1332px;width:283px;height:303px;background:linear-gradient(135deg,#8a6038,#d7b88f 50%,#efe6dc)}

/* loan programs */
.section-title{left:0;top:1700px;width:1200px;text-align:center;font-size:26px;font-weight:600;color:#333}
.program .img{width:100%}
.program h4{font-size:14px;font-weight:600;color:#222;margin-top:18px}
.program span{display:block;font-size:10px;color:#555;margin-top:8px}

/* contact */
.contact{left:0;top:2508px;width:1200px;height:388px;background:linear-gradient(90deg,#b9d2ea,#dfeaf4 40%,#c8d6e6 60%,#9db4d0)}
.contact-photo{left:636px;top:0;width:564px;height:388px;background:linear-gradient(120deg,#dfe7f1,#a9bedb 50%,#3b6fd6 60%,#c9d6e6 80%)}
.form{left:150px;top:0;width:486px;height:388px;background:rgba(240,246,252,.75);padding:22px 14px}
.form h2{font-size:29px;font-weight:600;color:#222;margin-left:6px}
.field{width:458px;height:34px;border:1px solid #c8ced6;border-radius:17px;background:#fff;font-size:12px;color:#888;padding:0 22px;display:flex;align-items:center;margin-top:18px}
.field.big{height:132px;border-radius:14px;align-items:flex-start;padding-top:14px}
.send{width:104px;height:30px;border-radius:15px;background:var(--blue-bright);color:#fff;font-size:13px;display:flex;align-items:center;justify-content:center;margin-top:20px}

/* footer */
.footer{left:0;top:2896px;width:1200px;height:221px;background:var(--dark);color:#eee}
.finfo{left:150px;font-size:12px;display:flex;align-items:center;gap:8px}
.fsocial{left:150px;top:135px;display:flex;gap:4px}
.fsocial span{width:30px;height:28px;display:block}
.footer h5{font-size:17px;font-weight:600;color:#fff}
.links{font-size:11px;line-height:22px}
.news-input{left:645px;top:83px;width:345px;height:52px;background:#fff;color:#888;font-size:11px;padding:0 20px;display:flex;align-items:center}
.news-btn{left:990px;top:83px;width:60px;height:52px;background:var(--blue-bright);display:flex;align-items:center;justify-content:center}
.bottom{left:0;top:3117px;width:1200px;height:50px;background:var(--darker);color:#ddd;font-size:11px;text-align:center;line-height:50px}
</style>
</head>
<body>

<header class="abs topbar">
  <div class="abs item" style="left:150px">
    <svg width="12" height="10" viewBox="0 0 12 10"><rect x=".5" y=".5" width="11" height="9" fill="none" stroke="#1f6fe0"/><path d="M.5 .5 6 5l5.5-4.5" fill="none" stroke="#1f6fe0"/></svg>
    <span><b>Email:</b> info@corvanelending.com</span>
  </div>
  <div class="abs item" style="left:373px">
    <svg width="11" height="11" viewBox="0 0 11 11"><path d="M2 1l2 2-1 1.5c.8 1.6 1.9 2.7 3.5 3.5L8 7l2 2-1.5 1.5C4.5 10 1 6.5.5 2.5z" fill="#1f6fe0"/></svg>
    <span><b>Phone:</b> (22) 555 0147</span>
  </div>
  <div class="abs item" style="left:842px;font-size:10px"><b>Connect With Us:</b></div>
  <div class="abs social-dots" style="right:150px">
    <span class="dot"></span><span class="dot"></span><span class="dot"></span><span class="dot"></span>
  </div>
</header>

<nav class="abs nav">
  <div class="abs brand"><span class="mark"></span><span class="name">Corvane Lending Partners</span></div>
  <div class="abs menu">
    <a class="active">Home</a><a>About Us</a><a>Loan Programs</a><a>Loan Closing</a><a>Loan Criteria</a><a>News</a><a>Contacts</a>
  </div>
  <a class="abs apply">Apply Now</a>
</nav>

<section class="abs hero" role="img" aria-label="Two businessmen in suits reviewing documents together in a bright office"></section>
<div class="abs hero-box">
  <div class="lead">Making Your</div>
  <h1>Business Ideas Come True</h1>
  <p>Praesent purus leo, ultrices et ligula ac, consectetur hendrerit nisl. Phasellus mollis dui dolor.</p>
  <a class="btn-dark">Get Started Now</a>
</div>

<section>
  <div class="abs feature" style="left:156px">
    <div class="diamond"><svg width="56" height="56" viewBox="0 0 56 56" fill="none" stroke="#2a7cf0" stroke-width="2"><circle cx="32" cy="16" r="9"/><path d="M32 11v10M29 14h5M29 18h5"/><path d="M6 38h8l6-4h10a3 3 0 010 6H22M30 40l12-8a3 3 0 014 4L32 46H12"/></svg></div>
    <h3>Debt Consolidations</h3>
    <p>Pellentesque habitant morbi tristique senectus et netus et malesuada fames ac turpis egestas.</p>
  </div>
  <div class="abs feature" style="left:465px">
    <div class="diamond"><svg width="66" height="56" viewBox="0 0 66 56" fill="none" stroke="#2a7cf0" stroke-width="2"><circle cx="20" cy="22" r="16"/><path d="M15 18a5 5 0 119 3c-2 1-3 2-3 4M21 30v1"/><rect x="30" y="24" width="30" height="20" rx="2"/><path d="M38 34l5 5 9-9"/></svg></div>
    <h3>Operating Expenses</h3>
    <p>Pellentesque habitant morbi tristique senectus et netus et malesuada fames ac turpis egestas.</p>
  </div>
  <div class="abs feature" style="left:772px">
    <div class="diamond"><svg width="56" height="56" viewBox="0 0 56 56" fill="none" stroke="#2a7cf0" stroke-width="2"><path d="M20 36a14 14 0 1116 0v6H20z"/><path d="M22 46h12M24 50h8"/><circle cx="28" cy="24" r="6"/><path d="M28 14v4M28 30v4M18 24h4M34 24h4M10 12l3 2M46 12l-3 2M28 2v4"/></svg></div>
    <h3>Equipment Financing</h3>
    <p>Pellentesque habitant morbi tristique senectus et netus et malesuada fames ac turpis egestas.</p>
  </div>
</section>

<section>
  <div class="abs tile-photo-a" role="img" aria-label="Smiling businessman working on a laptop at a wooden desk"></div>
  <div class="abs deliver">
    <h2>WE DELIVER ENDURING<br>RESULTS</h2>
    <p>We're already up. Let us worry for you.</p>
    <a class="btn-blue">Explore <svg width="6" height="8" viewBox="0 0 6 8"><path d="M1 1l3 3-3 3" stroke="#fff" fill="none" stroke-width="1.5"/></svg></a>
  </div>
  <div class="abs tile-video">
    <h3>Our comprehensive video</h3>
    <p>onec euismod urna fringilla ex rhoncus, vitae sceleris-que sem elementum.</p>
    <svg class="abs play" width="60" height="60" viewBox="0 0 60 60" fill="none" stroke="#fff" stroke-width="2"><circle cx="30" cy="30" r="28"/><path d="M24 19l17 11-17 11z"/></svg>
  </div>
  <div class="abs tile-grey">
    <h3>Quisque condimentum <span>euismod sagittis</span></h3>
    <p>Vestibulum ante ipsum primis in faucibus orci luctus et ultrices posuere cubilia Curae; Integer rhoncus tellus vitae venenatis ullamcorper.</p>
    <a class="btn-outline">Know More <svg width="6" height="8" viewBox="0 0 6 8"><path d="M1 1l3 3-3 3" stroke="#222" fill="none" stroke-width="1.5"/></svg></a>
  </div>
  <div class="abs tile-violet">
    <h3>Class aptent taciti sociosqu torquent conubia</h3>
    <p>Pellentesque habitant morbi tristique senectus et netus et malesuada fames ac turpis egestas. Suspend-isse molestie quam quis enim porta commodo.</p>
    <a class="btn-white">Know More <svg width="6" height="8" viewBox="0 0 6 8"><path d="M1 1l3 3-3 3" stroke="#1f6fe0" fill="none" stroke-width="1.5"/></svg></a>
  </div>
  <div class="abs tile-photo-b" role="img" aria-label="Young woman smiling at her phone beside a laptop"></div>
</section>

<section>
  <h2 class="abs section-title">Loan Programs</h2>
  <div class="abs program" style="left:150px;top:1782px;width:593px">
    <div class="img" style="height:276px;background:linear-gradient(135deg,#1f2a38,#9fb6cf 45%,#dbe5ee 70%,#54708f)" role="img" aria-label="Looking up at glass office towers"></div>
    <h4>Office Loans</h4><span>Read More</span>
  </div>
  <div class="abs program" style="left:765px;top:1782px;width:285px">
    <div class="img" style="height:276px;background:linear-gradient(180deg,#6b8cc4,#a9c0e2 50%,#6e8f3c 70%,#4e8a22)" role="img" aria-label="Open green field with a farmhouse under a blue sky"></div>
    <h4>Land Loans</h4><span>Read More</span>
  </div>
  <div class="abs program" style="left:150px;top:2156px;width:285px">
    <div class="img" style="height:208px;background:linear-gradient(135deg,#2a1a10,#8a5a2a 50%,#3a2618)" role="img" aria-label="Guests at a warmly lit hotel bar"></div>
    <h4>Hospitality Loans</h4><span>Read More</span>
  </div>
  <div class="abs program" style="left:457px;top:2156px;width:286px">
    <div class="img" style="height:208px;background:linear-gradient(180deg,#e8eaea,#b9a88a 50%,#4f6a3a)" role="img" aria-label="Shopping mall atrium with palm trees under a glass dome"></div>
    <h4>Retail Loans</h4><span>Read More</span>
  </div>
  <div class="abs program" style="left:765px;top:2156px;width:285px">
    <div class="img" style="height:208px;background:linear-gradient(135deg,#3d4a66,#b8c3d2 50%,#e5e8ee)" role="img" aria-label="Industrial plant floor with large steel pipes"></div>
    <h4>Industrial Loans</h4><span>Read More</span>
  </div>
</section>

<section class="abs contact" role="img" aria-label="Pale classical building facade">
  <div class="abs contact-photo" role="img" aria-label="Confident man in a blue suit carrying a briefcase"></div>
  <div class="abs form">
    <h2>Get In Touch</h2>
    <div class="field">Name</div>
    <div class="field">E-mail</div>
    <div class="field big">Message</div>
    <div class="send">SEND</div>
  </div>
</section>

<footer class="abs footer">
  <div class="abs finfo" style="top:45px">
    <svg width="24" height="22" viewBox="0 0 24 22" fill="none" stroke="#fff" stroke-width="1.5"><circle cx="12" cy="11" r="9"/><path d="M3 15l-2 5 5-2"/><text x="7" y="14" font-size="7" fill="#fff" stroke="none">24</text></svg>
    Call Us: (22) 555 0147
  </div>
  <div class="abs finfo" style="top:92px">
    <svg width="22" height="15" viewBox="0 0 22 15" fill="none" stroke="#fff" stroke-width="1.3"><rect x=".7" y=".7" width="20.6" height="13.6"/><path d="M.7 .7 11 8 21.3.7M.7 14.3l7-7M21.3 14.3l-7-7"/></svg>
    Mail Us: info@corvanelending.com
  </div>
  <div class="abs fsocial">
    <span style="background:#3b5a9a"></span><span style="background:#c8232c"></span><span style="background:#d6336c"></span><span style="background:#1da1f2"></span><span style="background:#dd4b39"></span>
  </div>
  <h5 class="abs" style="left:417px;top:40px">Quick Links</h5>
  <div class="abs links" style="left:420px;top:79px">Home<br>About Us<br>Loan Programs<br>Loan Closing</div>
  <div class="abs links" style="left:523px;top:79px">Loan Criteria<br>News<br>Contacts</div>
  <h5 class="abs" style="left:645px;top:40px">Newsletter Subscribe</h5>
  <div class="abs news-input">Enter Your Mail Id</div>
  <div class="abs news-btn"><svg width="28" height="24" viewBox="0 0 28 24"><path d="M1 11 27 1 21 23l-7-7-4 5v-7L24 4 8 13z" fill="#fff"/></svg></div>
</footer>
<div class="abs bottom">© 2018 Corvanelending. All Rights Reserved | Privacy Policy</div>

</body>
</html>
```